Riverbend Strong Unions and Households Project-Postcard

We need a postcard to promote our program. We will use the postcard to remind clients of appointments or even use it as a marketing tool when we go out to events. We provide healthy relationship education, financial classes and job readiness education. Our target population is adult couples. Mostly Spanish speaking. If its possible to incorporate all three components into the design that would be great, if not, healthy relationship would be our priority.

Attached is a logo we would like to use.

I have also included the text we would like to use. Would you please make all text editable incase we want to add different text.

The funding statement has to go at the bottom (it can be in small text).

Industry/Entity Type

Marketing

Requirements
Must have
• if you use images of people, please use Latino images. Our target population is Spanish speaking.

```html
<!DOCTYPE html>
<html lang="es">
<head>
<meta charset="utf-8">
<title>Riverbend Strong Unions and Households Project – Postcard</title>
<link href="https://fonts.googleapis.com/css2?family=Fira+Sans:ital,wght@0,400;0,600;0,700;1,700&family=Fira+Sans+Condensed:ital,wght@0,700;1,700&family=Fjalla+One&family=Arimo&display=swap" rel="stylesheet">
<style>
  :root {
    --stage: #2e2a27;
    --paper: #ffffff;
    --navy: #2a2f8c;
    --blue: #1f4e9c;
    --blue-deep: #173a7e;
    --crimson: #c9184f;
    --orange: #f39a1d;
    --slot: #e6e7e9;
    --ink: #1a1a1a;
    --tint: #fbf3f3;
  }
  * { box-sizing: border-box; margin: 0; padding: 0; }
  html, body { width: 863px; height: 1200px; overflow: hidden; background: var(--stage); }
  .stage { position: relative; width: 863px; height: 1200px; }

  .card { position: absolute; left: 86px; width: 683px; height: 530px; background: var(--paper); overflow: hidden; }
  .card--front { top: 54px; }
  .card--back { top: 608px; background: var(--tint); }

  /* Front */
  .photo { position: absolute; }
  .photo--family { left: 14px; top: 26px; width: 510px; height: 400px;
    background: radial-gradient(ellipse at 50% 45%, #e9eef5 0%, #dfe5ee 45%, #ffffff 80%); }
  .placard { position: absolute; left: 112px; top: 180px; width: 310px; height: 160px; background: var(--paper);
    display: flex; flex-direction: column; align-items: center; justify-content: center; gap: 4px; }
  .placard__name { font-family: "Fira Sans", sans-serif; font-weight: 700; font-size: 23px; line-height: 1.1; color: var(--navy); text-align: center; }
  .placard__mark { width: 22px; height: 22px; border-radius: 50%; background: var(--crimson); }
  .banner { position: absolute; left: 112px; top: 330px; width: 312px; height: 88px; background: var(--crimson);
    transform: rotate(-1deg); display: flex; align-items: center; justify-content: center; }
  .banner__text { font-family: "Fira Sans Condensed", sans-serif; font-style: italic; font-weight: 700; font-size: 25px; line-height: 1.25; color: #fff; text-align: center; }

  .contact { position: absolute; right: 28px; top: 22px; text-align: right; color: var(--navy); font-family: "Fira Sans", sans-serif; }
  .contact__lead { font-style: italic; font-weight: 700; font-size: 19px; }
  .contact__phone { font-weight: 700; font-size: 38px; line-height: 1.2; letter-spacing: 0.5px; }
  .program { position: absolute; right: 28px; top: 108px; width: 210px; text-align: right; font-family: "Fira Sans", sans-serif; }
  .program__name { font-size: 13px; font-weight: 600; color: var(--orange); line-height: 1.2; }
  .program__tag { margin-top: 3px; font-size: 6.5px; color: var(--navy); letter-spacing: 0.3px; text-transform: uppercase; line-height: 1.3; }

  .waves { position: absolute; left: 0; top: 0; }
  .funding { position: absolute; left: 30px; right: 30px; top: 484px; font-family: "Fira Sans", sans-serif; font-size: 10.6px; line-height: 1.4; color: #fff; }

  .services { position: absolute; left: 476px; top: 292px; width: 178px; height: 178px; border-radius: 50%; overflow: hidden;
    background: var(--orange); border: 2px solid #fff; box-shadow: 0 2px 6px rgba(0,0,0,.25);
    text-align: center; font-family: "Fira Sans Condensed", sans-serif; font-weight: 700; color: #fff; }
  .services__title { background: var(--crimson); height: 48px; padding-top: 19px; font-size: 19px; line-height: 1.2; }
  .services__list { list-style: none; padding: 4px 14px 0; font-size: 15px; line-height: 1.2; }
  .services__list li { padding: 3px 0; border-bottom: 1px solid rgba(255,255,255,.75); }
  .services__list li:last-child { border-bottom: 0; }

  /* Back */
  .sweep { position: absolute; left: 0; top: 0; }
  .headline { position: absolute; left: 30px; top: 30px; font-family: "Fjalla One", sans-serif; font-size: 30px; line-height: 1.35; color: #fff; letter-spacing: 0.5px; }
  .photo--couple { left: 34px; top: 128px; width: 272px; height: 402px;
    background: linear-gradient(180deg, rgba(220,226,236,.95) 0%, #e8ebf0 55%, #f4f4f6 100%); border-radius: 40% 40% 0 0 / 18% 18% 0 0; }
  .slot { position: absolute; background: var(--slot); font-family: "Arimo", sans-serif; font-size: 19px; color: var(--ink); text-align: center; }
  .slot--postage { left: 514px; top: 18px; width: 152px; height: 152px; padding-top: 68px; line-height: 1.25; }
  .slot--address { left: 330px; top: 170px; width: 336px; height: 266px; padding-top: 40px; }
  .slot--barcode { left: 86px; top: 436px; width: 580px; height: 74px; padding-top: 38px; }
</style>
</head>
<body>
<main class="stage">

  <section class="card card--front" aria-label="Postcard front">
    <div class="photo photo--family" role="img" aria-label="Smiling Latino family of four holding a sign"></div>

    <div class="placard">
      <span class="placard__mark"></span>
      <p class="placard__name">Riverbend<br>Community Partners</p>
    </div>
    <div class="banner">
      <p class="banner__text">…porque una relación<br>sana estáasu alcance</p>
    </div>

    <div class="contact">
      <p class="contact__lead">Para más información, llame a</p>
      <p class="contact__phone">555-014-2280</p>
    </div>
    <div class="program">
      <p class="program__name">Riverbend Strong Unions and Households Project</p>
      <p class="program__tag">Fortalecimiento de relaciones | Capacitación financiera<br>y preparación laboral</p>
    </div>

    <svg class="waves" width="683" height="530" viewBox="0 0 683 530" aria-hidden="true">
      <path d="M0,428 Q260,478 683,398 L683,530 L0,530 Z" fill="var(--orange)"/>
      <path d="M420,472 Q580,440 683,418 L683,440 Q580,458 460,478 Z" fill="var(--crimson)"/>
      <path d="M0,462 Q320,482 683,432 L683,530 L0,530 Z" fill="var(--blue)"/>
    </svg>

    <div class="services">
      <p class="services__title">We Provide</p>
      <ul class="services__list">
        <li>Healthy Relationship<br>Education,</li>
        <li>Financial Classes,</li>
        <li>Job Readiness<br>Education</li>
      </ul>
    </div>

    <p class="funding">“Funding for this project was provided by the National Family Services Agency, Office for Children and Households, Grant: #00RB0000. These services are available to all eligible persons, regardless of race, gender, age, disability, or religion.”</p>
  </section>

  <section class="card card--back" aria-label="Postcard back">
    <svg class="sweep" width="683" height="530" viewBox="0 0 683 530" aria-hidden="true">
      <path d="M0,0 H425 C445,110 360,145 290,148 C220,152 190,200 180,260 C170,320 110,332 0,336 Z" fill="var(--blue)"/>
      <path d="M430,0 C452,118 368,152 292,156 C230,160 200,190 192,230" fill="none" stroke="var(--blue-deep)" stroke-width="1.5"/>
      <path d="M438,0 C462,124 372,160 296,164" fill="none" stroke="var(--blue-deep)" stroke-width="1"/>
      <path d="M0,324 Q60,322 100,318" fill="none" stroke="#ffffff" stroke-width="1.5"/>
    </svg>
    <p class="headline">…porque una relación<br>sana estáasu alcance</p>
    <div class="photo photo--couple" role="img" aria-label="Smiling Latino couple standing back to back"></div>

    <div class="slot slot--postage">Postage<br>Area</div>
    <div class="slot slot--address">Address Area</div>
    <div class="slot slot--barcode">Barcode Area</div>
  </section>

</main>
</body>
</html>
```